vintage lumivane thank you postcard

I am wanting to use this postcard for my wedding thank you. My theme is: outdoor, rustic, country, vintage, neutral colored. The photo booth at my wedding was in a grain bin on a old victorian couch photos taken with a digital lumivane camera! I want the post card to look like an old fashioned lumivane picture with the border and all. At the bottom saying "thank you" or "Reid and Marta," "Brodwick Wedding", "June 14, 2014," something to that affect. On the back left side leaving room for me to write a personal message thanking them for the help/gift/support. The back right side left for the name and address. I will add a wedding picture of the two of us to the front (from our wedding day). Anything that gives the post card a vintage old time feeling is great!! I have a general idea of what I want but, now I know you guys can take care of the rest for me! :) thank you in advance!! -Marta

Target Market(s)

family, friends - all ages!

Industry/Entity Type

Wedding

Requirements
Must have
• "lumivane photo" look
vintage
"Thank you"
"Reid and Marta"
Nice to have
• June 14, 2014

```html
<!DOCTYPE html>
<html lang="en">
<head>
<meta charset="utf-8">
<title>Reid &amp; Marta – Thank You Postcard</title>
<link href="https://fonts.googleapis.com/css2?family=Yellowtail&display=swap" rel="stylesheet">
<style>
  :root {
    --page: #ffffff;
    --card: #a9c8cb;
    --photo: #ffffff;
    --photo-edge: #b9b9b9;
    --ink-light: #ffffff;
    --ink-shadow: #2f6a6b;
    --rule: #ffffff;
  }
  html, body {
    margin: 0;
    padding: 0;
    overflow: hidden;
    background: var(--page);
  }
  .canvas {
    position: relative;
    width: 1200px;
    height: 900px;
    overflow: hidden;
    background: var(--page);
  }
  .card {
    position: absolute;
    background: var(--card);
  }
  .card-front {
    left: 182px;
    top: 207px;
    width: 391px;
    height: 477px;
  }
  .card-back {
    left: 662px;
    top: 215px;
    width: 388px;
    height: 474px;
  }
  .card-texture {
    position: absolute;
    inset: 0;
    background: var(--card);
  }
  .photo-window {
    position: absolute;
    left: 24px;
    top: 27px;
    width: 343px;
    height: 351px;
    background: var(--photo);
    box-shadow: inset -2px 2px 0 var(--photo-edge);
  }
  .script {
    position: absolute;
    margin: 0;
    font-family: "Yellowtail", cursive;
    font-weight: 400;
    color: var(--ink-light);
    text-shadow: 2px 2px 0 var(--ink-shadow);
    white-space: nowrap;
    text-align: center;
    line-height: 1;
  }
  .thank-you {
    left: 0;
    width: 100%;
    top: 398px;
    font-size: 54px;
    transform: rotate(-4deg);
  }
  .couple-names {
    left: 0;
    width: 100%;
    top: 40px;
    font-size: 32px;
    transform: rotate(-4deg);
  }
  .back-layout {
    position: absolute;
    inset: 0;
  }
</style>
</head>
<body>
<main class="canvas">
  <section class="card card-front" aria-label="Postcard front">
    <div class="card-texture" role="img" aria-label="Soft polka dot pattern on dusty blue"></div>
    <div class="photo-window" role="img" aria-label="Space for the couple's wedding photo"></div>
    <h1 class="script thank-you">Thank you</h1>
  </section>

  <section class="card card-back" aria-label="Postcard back">
    <div class="card-texture" role="img" aria-label="Soft polka dot pattern on dusty blue"></div>
    <h2 class="script couple-names">Reid &amp; Marta</h2>
    <svg class="back-layout" width="388" height="474" viewBox="0 0 388 474" aria-hidden="true">
      <g stroke="var(--rule)" stroke-width="2" fill="none">
        <line class="divider" x1="194" y1="142" x2="194" y2="437"/>
        <line class="address-line" x1="217" y1="209" x2="370" y2="209"/>
        <line class="address-line" x1="217" y1="266" x2="370" y2="266"/>
        <line class="address-line" x1="217" y1="322" x2="370" y2="322"/>
      </g>
    </svg>
  </section>
</main>
</body>
</html>
```